New Business Card for Casual Beachfront Cafe

Quirky Beachfront Cafe at Moana, South Australia needs a DOUBLE SIDED business card to print on PressLoom.

Target Market(s)

Business Cards sit on the counter for Guests to take with them. Please view our website www.saltwhistlekitchen.com.au to get a feel for the Cafe. You may also view our Instagram at @saltwhistlekitchen

Industry/Entity Type

Cafe / Restaurant

Contact Information for Business Card

Information equivalent to: Breakfast, Lunch, Dinner, Coffee, Takeaway / 87 Tidewater Parade Corvale SA 5280 / Menu & Opening Hours: www.saltwhistlekitchen.com.au / ph (08) 8591 2736

Requirements
Must have
• Information equivalent to: Breakfast, Lunch, Dinner, Coffee, Takeaway / 87 Tidewater Parade Corvale SA 5280 / Menu & Opening Hours: www.saltwhistlekitchen.com.au / ph (08) 8591 2736
Nice to have
• Potentially some of our trademark colours (Cafe can be searched via Trovix)
Should not have
• Must NOT have image of the building. May have the logo provided on one side but not necessarily, depending on how you wish to design the card

```html
<!DOCTYPE html>
<html lang="en">
<head>
<meta charset="utf-8">
<title>Salt Whistle Kitchen — Business Card</title>
<link rel="stylesheet" href="https://fonts.googleapis.com/css2?family=Montserrat:wght@400;500;800;900&display=swap">
<style>
  :root {
    --stage: #2e2e30;
    --brand-blue: #1d5c8f;
    --sun-yellow: #f1ec1e;
    --rust-frame: #b9652b;
    --tag-orange: #c27a3c;
    --paper: #fbfbfb;
    --ink-grey: #4f4f55;
  }
  * { box-sizing: border-box; margin: 0; padding: 0; }
  html, body {
    width: 1200px; height: 1200px; overflow: hidden;
    background: var(--stage);
    font-family: "Montserrat", Arial, sans-serif;
  }
  .sheet {
    width: 1200px; height: 1200px;
    display: flex; flex-direction: column; align-items: center; justify-content: center;
    gap: 60px;
  }
  .card {
    width: 840px; height: 480px; position: relative; overflow: hidden;
    box-shadow: 0 10px 30px rgba(0,0,0,.45);
  }

  /* Front */
  .card--front {
    background: var(--sun-yellow);
    border: 20px solid var(--rust-frame);
  }
  .front__name {
    position: absolute; left: 0; right: 0; top: 46px;
    color: var(--brand-blue);
    font-weight: 900;
    text-transform: uppercase;
    text-align: center;
    line-height: .95;
    letter-spacing: -1px;
  }
  .front__name-top { display: block; font-size: 84px; }
  .front__name-main { display: block; font-size: 132px; margin-top: 6px; }
  .front__tagline {
    position: absolute; left: 60px; bottom: 34px;
    color: var(--tag-orange);
    font-size: 20px;
    font-weight: 500;
    letter-spacing: .5px;
  }

  /* Back */
  .card--back { background: var(--paper); }
  .back__brand {
    position: absolute; left: 70px; top: 50px;
    color: var(--brand-blue);
    font-weight: 900;
    text-transform: uppercase;
    line-height: .95;
  }
  .back__brand-top { display: block; font-size: 34px; }
  .back__brand-main { display: block; font-size: 52px; margin-top: 2px; }
  .back__person {
    position: absolute; right: 56px; top: 196px; text-align: right;
  }
  .person__name { color: var(--brand-blue); font-weight: 800; font-size: 34px; line-height: 1.1; }
  .person__role { color: var(--ink-grey); font-size: 20px; margin-top: 2px; }
  .back__rule {
    position: absolute; left: 56px; right: 56px; top: 276px;
    height: 2px; background: var(--brand-blue);
  }
  .contact-list {
    position: absolute; list-style: none;
    color: var(--ink-grey); font-size: 19px; line-height: 1.3;
  }
  .contact-list--left { left: 56px; top: 300px; }
  .contact-list--right { left: 470px; top: 300px; }
  .contact-list li { display: flex; align-items: flex-start; gap: 12px; margin-bottom: 10px; }
  .contact-list svg { flex: none; width: 18px; height: 18px; margin-top: 3px; fill: var(--brand-blue); }
  .social-dot { flex: none; width: 16px; height: 16px; margin: 4px 1px 0; border-radius: 50%; background: var(--brand-blue); }
</style>
</head>
<body>
<main class="sheet">
  <section class="card card--front">
    <h1 class="front__name"><span class="front__name-top">Salt Whistle</span><span class="front__name-main">Kitchen</span></h1>
    <p class="front__tagline">Breakfast | Lunch | Dinner | Coffee | Takeaway</p>
  </section>

  <section class="card card--back">
    <div class="back__brand"><span class="back__brand-top">Salt Whistle</span><span class="back__brand-main">Kitchen</span></div>

    <div class="back__person">
      <p class="person__name">Marlen Okafor</p>
      <p class="person__role">Director</p>
    </div>

    <div class="back__rule"></div>

    <ul class="contact-list contact-list--left">
      <li>
        <svg viewBox="0 0 24 24" aria-hidden="true"><path d="M6.6 10.8a15.1 15.1 0 0 0 6.6 6.6l2.2-2.2a1 1 0 0 1 1-.25 11.4 11.4 0 0 0 3.6.57 1 1 0 0 1 1 1V20a1 1 0 0 1-1 1A17 17 0 0 1 3 4a1 1 0 0 1 1-1h3.5a1 1 0 0 1 1 1c0 1.25.2 2.45.57 3.57a1 1 0 0 1-.25 1z"/></svg>
        <span>(08) 8591 2736</span>
      </li>
      <li>
        <svg viewBox="0 0 24 24" aria-hidden="true"><path d="M2 5h20v14H2z M2 5l10 8 10-8" fill="none" stroke="#1d5c8f" stroke-width="2"/><path d="M2 5h20l-10 8z"/></svg>
        <span>marlen@saltwhistlekitchen.com</span>
      </li>
      <li>
        <svg viewBox="0 0 24 24" aria-hidden="true"><circle cx="12" cy="12" r="9.5" fill="none" stroke="#1d5c8f" stroke-width="2"/><path d="M2.5 12h19M12 2.5c-3 3-3 16 0 19M12 2.5c3 3 3 16 0 19" fill="none" stroke="#1d5c8f" stroke-width="1.6"/></svg>
        <span>www.saltwhistlekitchen.com.au</span>
      </li>
    </ul>

    <ul class="contact-list contact-list--right">
      <li>
        <svg viewBox="0 0 24 24" aria-hidden="true"><path d="M12 2a7 7 0 0 0-7 7c0 5 7 13 7 13s7-8 7-13a7 7 0 0 0-7-7zm0 9.5A2.5 2.5 0 1 1 12 6.5a2.5 2.5 0 0 1 0 5z"/></svg>
        <span>87 Tidewater Parade Corvale<br>SA 5280</span>
      </li>
      <li>
        <span class="social-dot" aria-hidden="true"></span>
        <span>@saltwhistlekitchen</span>
      </li>
    </ul>
  </section>
</main>
</body>
</html>
```